Pecan Ridge Paving. Chip Seal Done Right

I need my card to have all my basic information on it. Keep it simple. Include web site, phone number and email address. Include phrase Chip Seal Done Right or Pecan Ridge’s Top Paving Company. Keep card simple. Include color and logo. Put all contact info on card. Make card simple and not complicated.

Here is infuriation yo out in business card

Dale R. Whitmore
830.555.0173 cell phone
Dalewhitmore7@mailbarn.net
www.pecanridgepaving.net

Target Market(s)

Hill Country Texas USA

Industry/Entity Type

Road chip seal

Contact Information for Business Card

We chip seal roads for ranches and property owners

Font styles to use
Serif
Sans Serif
Decorative
Script

Colors
0054AA
0677BA
7BADD7
CADEEF
E8F1F8
EB3D1F
EC4F4E
F09395
F8D3D4
FCEDEE

Requirements
Must have
• Keep it simply
Nice to have
• Logo and all basic info

```html
<!DOCTYPE html>
<html lang="en">
<head>
<meta charset="utf-8">
<title>Pecan Ridge Paving – Business Card</title>
<link rel="stylesheet" href="https://fonts.googleapis.com/css2?family=EB+Garamond:ital,wght@0,400;0,600;1,400;1,700&family=Montserrat:wght@500;800&display=swap">
<style>
  :root {
    --navy: #141c4a;
    --red: #ab1f2d;
    --ink: #1b2350;
    --grey-text: #555a63;
    --card-white: #ffffff;
    --backdrop: #dcdcdc;
  }
  * { margin: 0; padding: 0; box-sizing: border-box; }
  html, body {
    width: 1047px; height: 1200px; overflow: hidden;
    background: var(--backdrop);
  }
  .canvas { position: relative; width: 1047px; height: 1200px; }

  .card {
    position: absolute; left: 160px; width: 741px; height: 424px;
    box-shadow: 0 2px 6px rgba(0,0,0,0.18);
    overflow: hidden;
  }
  .card--front { top: 120px; background: var(--card-white); }
  .card--back { top: 634px; background: var(--navy); }

  /* Front */
  .identity {
    position: absolute; right: 389px; top: 158px; text-align: right;
    font-family: "EB Garamond", serif;
  }
  .identity__name {
    font-weight: 600; font-size: 29px; letter-spacing: 0.5px;
    color: var(--ink); text-transform: uppercase; line-height: 1;
  }
  .identity__title {
    font-size: 18px; color: var(--red); margin-top: 4px; line-height: 1;
  }
  .divider {
    position: absolute; left: 383px; top: 114px; width: 1.5px; height: 136px;
    background: var(--red);
  }
  .contact {
    position: absolute; left: 418px; top: 118px; list-style: none;
    font-family: "EB Garamond", serif; font-size: 17.5px; color: var(--grey-text);
    letter-spacing: 0.6px;
  }
  .contact__item { display: flex; align-items: flex-start; line-height: 24px; margin-bottom: 3px; }
  .contact__item--address { margin-bottom: 8px; }
  .contact__icon { width: 13px; height: 13px; margin: 5px 8px 0 0; flex: none; fill: var(--ink); }

  .tagline-band {
    position: absolute; left: 0; top: 326px; width: 741px; height: 42px;
    background: var(--navy);
  }
  .tagline-band__accent {
    position: absolute; right: 0; top: 0; width: 128px; height: 42px; background: var(--red);
  }
  .tagline-band__mark {
    position: absolute; left: 633px; top: 10px; width: 22px; height: 22px;
    border-radius: 50%; background: var(--card-white);
  }
  .tagline {
    position: absolute; left: 0; width: 760px; top: 0; line-height: 42px; text-align: center;
    font-family: "EB Garamond", serif; font-style: italic; font-size: 26px;
    color: var(--card-white);
  }
  .tagline strong { font-weight: 700; }

  /* Back */
  .brand__circle {
    position: absolute; left: 140px; top: 142px; width: 168px; height: 168px;
    border-radius: 50%; background: var(--red);
  }
  .brand__name {
    position: absolute; left: 335px; top: 124px;
    font-family: "Montserrat", sans-serif; font-weight: 800;
    font-size: 42px; line-height: 56px; color: var(--card-white); text-transform: uppercase;
    white-space: nowrap;
  }
  .brand__years {
    position: absolute; left: 335px; top: 250px; display: flex; align-items: center;
    font-family: "Montserrat", sans-serif; font-weight: 500; font-size: 16px;
    letter-spacing: 0.5px; color: var(--red); white-space: nowrap;
  }
  .brand__years::before {
    content: ""; width: 140px; height: 2px; background: var(--red); margin-right: 12px;
  }
</style>
</head>
<body>
<div class="canvas">

  <section class="card card--front" aria-label="Business card front">
    <div class="identity">
      <p class="identity__name">Dale R. Whitmore</p>
      <p class="identity__title">Founder &amp; CEO</p>
    </div>

    <div class="divider"></div>

    <ul class="contact">
      <li class="contact__item contact__item--address">
        <svg class="contact__icon" viewBox="0 0 12 12"><path d="M6 0a4 4 0 0 0-4 4c0 3 4 8 4 8s4-5 4-8a4 4 0 0 0-4-4zm0 5.6A1.6 1.6 0 1 1 6 2.4a1.6 1.6 0 0 1 0 3.2z"/></svg>
        <span>1234 Main Street<br>City, State &amp; ZIP code</span>
      </li>
      <li class="contact__item">
        <svg class="contact__icon" viewBox="0 0 12 12"><path d="M2.4 0.5l1.8 2.6-1 1.2c.7 1.6 2 2.9 3.5 3.6l1.2-1 2.6 1.8-.8 2.2C5 10.8 1.2 7 .3 1.4z"/></svg>
        <span>830.555.0173</span>
      </li>
      <li class="contact__item">
        <svg class="contact__icon" viewBox="0 0 12 12"><path d="M0 2.5h12v1L6 7 0 3.5zM0 4.8l6 3.4 6-3.4V10H0z"/></svg>
        <span>Dalewhitmore7@mailbarn.net</span>
      </li>
      <li class="contact__item">
        <svg class="contact__icon" viewBox="0 0 12 12"><circle cx="6" cy="6" r="6"/><path d="M3 3.5l2 .5 1 2-1.5 1 .5 2.5M8 2l1 2 1.5.5" stroke="#fff" stroke-width="1" fill="none"/></svg>
        <span>www.pecanridgepaving.net</span>
      </li>
    </ul>

    <div class="tagline-band">
      <div class="tagline-band__accent"></div>
      <div class="tagline-band__mark"></div>
      <p class="tagline">Chip Seal <strong>Done Right</strong></p>
    </div>
  </section>

  <section class="card card--back" aria-label="Business card back">
    <div class="brand__circle"></div>
    <p class="brand__name">Pecan Ridge<br>Paving</p>
    <p class="brand__years">OVER 40 YEARS</p>
  </section>

</div>
</body>
</html>
```